Business Card Needed for Crafter of Pottery, Jewelry and Artwork

Calling all designers in search of an artistic challenge.

I need a new business card design for my pottery, jewelry and artwork business, Woven Glass and Tide, based in Vancouver BC.

I would like a card that is bright and inviting and preferably incorporates my logo and a sample of photos of my work while having a clean fresh look. The following contact details would preferably be included on the card as well:
• Helena Pikeworth
• Designer
• Phone: 604.555.0172
• Email: Designer@WovenGlassandTide.example
• Website: www.WovenGlassandTide.example
• Blog: www.ShapingHillside.example

The logo is attached in two color schemes in both Vector and Source formats. On past cards I’ve also included photos of my work. By including photos of the work the pieces are showcased and it catches people’s eye and prompts them to pick up the card and look at it more closely. For example, if I leave a stack in a coffee shop I want people to be drawn to the card, to pick it up and get a sense of the my product lines. Please feel free to pull photos of my work directly off of my website. If you need photos with higher pixels please let me know and I’ll email them directly to you. The website background is bffbda (191, 251, 218). I would like the business cards to match the feel of the website for consistency but the cards do not need to use the exact same colors. My website and current business card are predominantly turquoise shades. The background uses stripes provided by the website template. I don’t know the exact colors of the stripes.

My current business card is attached to show the use of photos in a design. Please note that I am not thrilled with my own design and am looking for variations and completely new designs. This example is not meant to be used as a template or starting point.

Here is some background surrounding my company:
WGT offers one of a kind jewelry, pottery, artwork and leather bags each designed with a twist. The pottery varies from rustic every day functional ware to raku artwork. The jewelry ranges from simple sterling every day pieces to multimedia pieces incorporating stone, metal, ceramics and fabric. The artwork is multimedia, typically acrylic paired with a natural element such as bark. All the bags are leather with reworked kimono fabric or patterned silk lining.

Feel free to check out my website to get a flavour for my work and the color scheme I've used on marketing materials so far. www.wovenglassandtide.example
Updates

Thank you to everyone who has submitted a design so far. I hope everyone has received some helpful feedback.

I'm going to post a survey to customers and friends asking for their votes. If you have new designs to submit please try to get them in by Saturday March 30 at noon so that I can include it in the survey launch.

Thank you

Target Market(s)

Females aged 25-65 interested in one of a kind functional pottery and jewelry.

Industry/Entity Type

Coffee Shop

Requirements
Must have
• Contact information, website, blog
Nice to have
• Logo, photos

```html
<!DOCTYPE html>
<html lang="en">
<head>
<meta charset="utf-8">
<title>Woven Glass and Tide – Business Card</title>
<link rel="stylesheet" href="https://fonts.googleapis.com/css2?family=Crimson+Pro:wght@400;700&display=swap">
<style>
  :root {
    --page: #efece7;
    --mint: #c2f7de;
    --navy: #24245e;
    --ink: #262a5a;
    --teal: #4fbfb6;
    --violet: #3a3aa2;
    --frame: #111111;
    --white: #ffffff;
    --blog: #f07a2c;
  }
  * { box-sizing: border-box; margin: 0; padding: 0; }
  html, body { width: 1200px; height: 1037px; overflow: hidden; }
  body {
    position: relative;
    background: var(--page);
    font-family: "Crimson Pro", Georgia, serif;
    color: var(--ink);
  }
  .card {
    position: absolute;
    width: 822px;
    height: 469px;
    background: var(--mint);
    overflow: hidden;
  }
  .card-front { left: 35px; top: 31px; }
  .card-back { left: 342px; top: 533px; }

  .front-waves { position: absolute; inset: 0; }

  .brand-ring {
    position: absolute;
    left: 47px; top: 48px;
    width: 296px; height: 296px;
    border: 3px solid var(--teal);
    border-radius: 50%;
    display: flex;
    align-items: center;
    justify-content: center;
    text-align: center;
  }
  .brand-name {
    font-size: 34px;
    font-weight: 400;
    letter-spacing: 3px;
    line-height: 1.15;
    text-transform: uppercase;
    color: var(--navy);
  }

  .contact-list {
    position: absolute;
    left: 413px; top: 100px;
    list-style: none;
    font-size: 22px;
    line-height: 34px;
    color: var(--ink);
  }
  .contact-list li { display: flex; align-items: center; gap: 10px; }
  .contact-icon { width: 18px; height: 18px; flex: none; }

  .person {
    position: absolute;
    right: 48px; top: 382px;
    text-align: right;
    color: var(--white);
  }
  .person-name { font-size: 31px; font-weight: 700; line-height: 1.1; }
  .person-role { font-size: 23px; font-weight: 400; line-height: 1.3; }

  .back-title {
    position: absolute;
    left: 0; right: 0; top: 4px;
    text-align: center;
    font-size: 29px;
    letter-spacing: 6.5px;
    font-weight: 400;
    color: var(--ink);
    text-transform: uppercase;
  }
  .work-grid {
    position: absolute;
    left: 21px; top: 57px;
    display: grid;
    grid-template-columns: repeat(3, 246px);
    grid-template-rows: repeat(2, 166px);
    column-gap: 22px;
    row-gap: 15px;
  }
  .work-photo {
    border: 3px solid var(--frame);
    border-radius: 24px;
  }
  .work-mugs { background: linear-gradient(180deg, #e9eeec 0%, #7fb3b2 45%, #3d4a4a 100%); }
  .work-necklace { background: linear-gradient(160deg, #d8d2c8 0%, #d6a08e 55%, #b5583a 100%); }
  .work-jar { background: radial-gradient(ellipse at 50% 55%, #2e4f9e 0%, #22407f 55%, #e6e2da 100%); }
  .work-bowl { background: radial-gradient(ellipse at 50% 50%, #5f9f85 0%, #8ab9a8 55%, #8a6a45 100%); }
  .work-bag { background: linear-gradient(180deg, #f1eeec 0%, #e0584c 40%, #c94238 100%); }
  .work-earrings { background: linear-gradient(135deg, #6b5a48 0%, #e8e4de 50%, #e55a87 75%, #a8dcc7 100%); }

  .back-url {
    position: absolute;
    left: 0; right: 0; top: 420px;
    text-align: center;
    font-size: 21px;
    letter-spacing: 3px;
    color: var(--ink);
  }
</style>
</head>
<body>

<section class="card card-front">
  <svg class="front-waves" viewBox="0 0 822 469" width="822" height="469" aria-hidden="true">
    <path fill="var(--teal)" d="M0,412 C100,450 230,466 380,455 L380,469 L0,469 Z"/>
    <path fill="var(--violet)" d="M0,362 C70,400 170,438 280,448 C180,454 80,432 0,402 Z"/>
    <path fill="var(--teal)" d="M285,469 C450,428 620,330 822,262 L822,292 C610,382 455,442 312,469 Z"/>
    <path fill="var(--navy)" d="M312,469 C455,442 610,382 822,292 L822,469 Z"/>
    <path fill="var(--violet)" d="M618,322 C700,292 762,262 822,232 L822,252 C760,278 700,302 618,322 Z"/>
  </svg>

  <div class="brand-ring">
    <p class="brand-name">Woven Glass<br>and Tide</p>
  </div>

  <ul class="contact-list">
    <li>
      <svg class="contact-icon" viewBox="0 0 18 18" aria-hidden="true"><circle cx="9" cy="9" r="8" fill="none" stroke="var(--ink)" stroke-width="1.5"/><path d="M6 5 L8 7 L7 8.5 C7.8 10 8.5 10.8 9.8 11.5 L11 10.5 L13 12.5 L11.5 14 C8 13 5.5 10 4.8 6.5 Z" fill="var(--ink)"/></svg>
      <span>604.555.0172</span>
    </li>
    <li>
      <svg class="contact-icon" viewBox="0 0 18 18" aria-hidden="true"><rect x="1.5" y="4" width="15" height="10" fill="none" stroke="var(--ink)" stroke-width="1.6"/><path d="M1.5 4 L9 10 L16.5 4" fill="none" stroke="var(--ink)" stroke-width="1.6"/></svg>
      <span>Designer@WovenGlassandTide.example</span>
    </li>
    <li>
      <svg class="contact-icon" viewBox="0 0 18 18" aria-hidden="true"><g fill="none" stroke="var(--ink)" stroke-width="1.3"><circle cx="9" cy="9" r="7.5"/><ellipse cx="9" cy="9" rx="3.3" ry="7.5"/><path d="M1.5 9 H16.5 M3 5 H15 M3 13 H15"/></g></svg>
      <span>www.WovenGlassandTide.example</span>
    </li>
    <li>
      <svg class="contact-icon" viewBox="0 0 18 18" aria-hidden="true"><rect x="1" y="1" width="16" height="16" rx="3" fill="var(--blog)"/></svg>
      <span>www.ShapingHillside.example</span>
    </li>
  </ul>

  <div class="person">
    <p class="person-name">Helena Pikeworth</p>
    <p class="person-role">Designer</p>
  </div>
</section>

<section class="card card-back">
  <h1 class="back-title">Woven Glass and Tide</h1>
  <div class="work-grid">
    <div class="work-photo work-mugs" role="img" aria-label="Photo of three turquoise and charcoal glazed pottery mugs"></div>
    <div class="work-photo work-necklace" role="img" aria-label="Photo of a peach stone bead necklace with a wooden pendant"></div>
    <div class="work-photo work-jar" role="img" aria-label="Photo of a round speckled blue glazed lidded jar"></div>
    <div class="work-photo work-bowl" role="img" aria-label="Photo of a pierced green glazed ceramic bowl"></div>
    <div class="work-photo work-bag" role="img" aria-label="Photo of a red leather tote bag with black straps"></div>
    <div class="work-photo work-earrings" role="img" aria-label="Photo of pink beaded earrings with mint drops hanging on bark"></div>
  </div>
  <p class="back-url">www.WovenGlassandTide.example</p>
</section>

</body>
</html>
```